Stationery design for online marketing company
Vumor
Stationery design for online marketing company - Marketing
Creative Brief
Use specific fonts
Feel free
Bright & Fun-filled
Ruth K. Dallimore
Project Director
Vumor Online Market Ltd 17 Marlowe Ridge Street Pelvine District Abuja, Nigeria
ruth@vumor.com
www.vumor.com
RC5073316
tepluwin tepluwin
Dear All, Please, you may want to include the letterhead design, email signature design etc

```html
<!DOCTYPE html>
<html lang="en">
<head>
<meta charset="utf-8">
<title>Vumor Business Card</title>
<link href="https://fonts.googleapis.com/css2?family=Comfortaa:wght@400;600;700&display=swap" rel="stylesheet">
<style>
  :root {
    --page: #ffffff;
    --card: #000000;
    --blue: #4f8ff0;
    --orange: #f2601c;
    --amber: #f5a623;
    --gold: #f0c233;
    --white: #ffffff;
    --glow: #3a8dff;
  }
  html, body {
    margin: 0;
    padding: 0;
    width: 1200px;
    height: 887px;
    overflow: hidden;
    background: var(--page);
    font-family: "Comfortaa", sans-serif;
  }
  .card {
    position: absolute;
    left: 300px;
    top: 271px;
    width: 600px;
    height: 341px;
    background: var(--card);
    box-shadow: 0 2px 6px rgba(0,0,0,0.25);
  }
  .brand {
    position: absolute;
    left: 84px;
    top: 140px;
    display: flex;
    flex-direction: column;
    align-items: flex-end;
  }
  .brand-row {
    display: flex;
    align-items: center;
    gap: 8px;
  }
  .brand-dot {
    width: 14px;
    height: 14px;
    border-radius: 50%;
    background: var(--orange);
  }
  .brand-name {
    font-size: 40px;
    font-weight: 700;
    color: var(--orange);
    line-height: 1;
  }
  .brand-tagline {
    font-size: 9px;
    color: var(--amber);
    margin-top: 3px;
    letter-spacing: 0.2px;
  }
  .divider {
    position: absolute;
    left: 299px;
    top: 45px;
    width: 2px;
    height: 240px;
    background: linear-gradient(to bottom, transparent, var(--glow) 25%, #9fd0ff 50%, var(--glow) 75%, transparent);
    box-shadow: 0 0 8px var(--glow);
  }
  .details {
    position: absolute;
    left: 360px;
    top: 76px;
    color: var(--orange);
  }
  .person-name {
    font-size: 20px;
    font-weight: 700;
    margin: 0;
    line-height: 1.1;
  }
  .person-name .first { color: var(--blue); }
  .person-name .rest { color: var(--orange); }
  .person-title {
    font-size: 13px;
    font-weight: 600;
    color: var(--amber);
    margin: 3px 0 14px;
  }
  .address, .phones {
    font-size: 10px;
    line-height: 1.35;
    margin: 0 0 10px;
  }
  .address { color: var(--amber); }
  .phones { color: var(--gold); }
  .license {
    font-size: 10px;
    color: var(--orange);
    margin: 0;
  }
  .email {
    font-size: 8px;
    color: var(--white);
    margin: 3px 0 0;
  }
</style>
</head>
<body>
  <div class="card">
    <div class="brand">
      <div class="brand-row">
        <span class="brand-dot"></span>
        <span class="brand-name">Vumor</span>
      </div>
      <span class="brand-tagline">shop wise, ship quick</span>
    </div>

    <div class="divider"></div>

    <div class="details">
      <p class="person-name"><span class="first">Ruth </span><span class="rest">K. Dallimore</span></p>
      <p class="person-title">Project Director</p>
      <p class="address">Vumor Online Market Ltd<br>17 Marlowe Ridge Street<br>Pelvine District<br>Abuja, Nigeria</p>
      <p class="phones">Toll-Free: 0800 412 7755<br>Phone: 0805 619 2047<br>Cell: 0803 574 918</p>
      <p class="license">License No: RC5073316</p>
      <p class="email">Email: ruth@vumor.com</p>
    </div>
  </div>
</body>
</html>
```